Criação de Papelaria Profissional para Beleza
A empresa queria:
" Atendemos clientes adultos masculino, feminino, adolescentes para tratamentos estéticos diversos como acne, rejuvenescimento facial, redução de medidas faciais e corporais, depilação, tratamento de celulite, estrias, medicina capilar, laser, cicatrizes, manchas, melasma, pequenos vasos, poros dilatados, limpeza de pele "

```html
<!DOCTYPE html>
<html lang="pt-BR">
<head>
<meta charset="utf-8">
<title>Lumiera Clínica Estética – Cartões</title>
<link rel="stylesheet" href="https://fonts.googleapis.com/css2?family=Montserrat:wght@400;500;600;700&display=swap">
<style>
  :root {
    --teal: #20b2a7;
    --teal-light: #3cc6bb;
    --teal-dark: #0f8c85;
    --navy: #1c2b58;
    --card-white: #ffffff;
    --card-grey: #eceff1;
    --field-text: #3d4f66;
    --page: #ffffff;
  }
  * { margin: 0; padding: 0; box-sizing: border-box; }
  html, body {
    width: 1200px; height: 1200px; overflow: hidden;
    background: var(--page);
    font-family: "Montserrat", sans-serif;
  }
  .canvas { position: relative; width: 1200px; height: 1200px; }

  .card {
    position: absolute; left: 197px; width: 806px;
    border-radius: 20px; overflow: hidden;
    box-shadow: 0 6px 14px rgba(0,0,0,0.18);
  }

  /* Front */
  .card-front {
    top: 139px; height: 442px;
    background: linear-gradient(180deg, var(--card-white) 0%, var(--card-white) 55%, var(--card-grey) 100%);
  }
  .front-rule {
    position: absolute; left: 0; right: 0; bottom: 36px; height: 4px;
    background: var(--teal-light);
  }
  .front-band {
    position: absolute; left: 0; right: 0; bottom: 0; height: 29px;
    background: linear-gradient(90deg, var(--teal-dark), var(--teal));
  }
  .brand-dot {
    position: absolute; left: 150px; top: 148px;
    width: 70px; height: 70px; border-radius: 50%;
    background: var(--teal);
  }
  .front-name {
    position: absolute; left: 270px; top: 138px;
    font-weight: 600; font-size: 84px; line-height: 1;
    color: var(--navy); letter-spacing: 1px; white-space: nowrap;
  }
  .front-tagline {
    position: absolute; left: 274px; top: 262px;
    font-weight: 600; font-size: 27px; letter-spacing: 5px;
    color: var(--teal-dark); white-space: nowrap;
  }

  /* Back */
  .card-back {
    top: 612px; height: 432px;
    background: linear-gradient(135deg, var(--teal-light) 0%, var(--teal) 50%, var(--teal-dark) 100%);
    color: #fff;
  }
  .back-brand { position: absolute; left: 100px; top: 30px; white-space: nowrap; }
  .back-name {
    font-weight: 500; font-size: 44px; line-height: 1; letter-spacing: 1px;
  }
  .back-tagline {
    margin-top: 8px; font-size: 14px; letter-spacing: 3px; font-weight: 400;
  }
  .promo {
    position: absolute; left: 89px; width: 340px; top: 164px;
    text-align: center; font-size: 14px; line-height: 1.35; font-weight: 400;
  }
  .website {
    position: absolute; left: 74px; width: 370px; top: 218px;
    text-align: center; font-size: 21px; font-weight: 700;
  }
  .social {
    position: absolute; left: 74px; width: 370px; top: 254px;
    display: flex; justify-content: center; gap: 22px;
    font-size: 11px; font-weight: 500;
  }
  .social span { display: inline-flex; align-items: center; gap: 6px; }
  .social i {
    display: inline-block; width: 11px; height: 11px; border-radius: 50%;
    background: #fff;
  }
  .stamp {
    position: absolute; width: 101px; height: 84px;
    background: #fff; border-radius: 2px;
  }
  .field {
    position: absolute; height: 39px; background: #fff;
    color: var(--field-text); font-size: 15px;
    padding: 9px 10px; line-height: 21px;
  }
</style>
</head>
<body>
<main class="canvas">

  <section class="card card-front" aria-label="Frente do cartão">
    <span class="brand-dot"></span>
    <span class="front-name">LUMIERA</span>
    <div class="front-tagline">CLÍNICA ESTÉTICA</div>
    <div class="front-rule"></div>
    <div class="front-band"></div>
  </section>

  <section class="card card-back" aria-label="Verso do cartão fidelidade">
    <div class="back-brand">
      <div class="back-name">LUMIERA</div>
      <div class="back-tagline">CLÍNICA ESTÉTICA</div>
    </div>

    <p class="promo">Aqui vai ser colocado a sua promomoção pra<br>o cartão fidelidade</p>
    <p class="website">www.LUMIERA.com.br</p>
    <div class="social">
      <span><i></i>/lumiera</span>
      <span><i></i>@lumiera</span>
    </div>

    <div class="stamp" style="left:440px; top:108px;"></div>
    <div class="stamp" style="left:564px; top:108px;"></div>
    <div class="stamp" style="left:688px; top:108px;"></div>
    <div class="stamp" style="left:440px; top:214px;"></div>
    <div class="stamp" style="left:564px; top:214px;"></div>
    <div class="stamp" style="left:688px; top:214px;"></div>

    <div class="field" style="left:55px; top:316px; width:734px;">Nome</div>
    <div class="field" style="left:55px; top:372px; width:348px;">Tel.</div>
    <div class="field" style="left:415px; top:372px; width:374px;">Nasc.</div>
  </section>

</main>
</body>
</html>
```